Improvement of design for elearning template

Our company provides web based elearning courses for employees. We have a design layout for the different slides which can be found here: https://www.filevault-example.com/sh/qk4rmtp8zy2bnel/BXcQuPeMdKtLwZrnaHv71sGtuQ?dl=0. The content will be added later. At this point we are just looking for a design layout that works with different content types like images, text, quiz & videos. What we would ask you, is to pick randomly 1 or 2 of the elearning slides from the existing designs and suggest improvements or come up with an alternative design. The winner of the design project can work on all slides and this will be a project with a much larger budget.
Target Market(s)
Employees in large enterprises
Look and feel
Each slider illustrates characteristics of the customer's brand and the style your logo design should communicate.

```html
<!DOCTYPE html>
<html lang="en">
<head>
<meta charset="utf-8">
<title>Handling sensitive information – Course start</title>
<link rel="stylesheet" href="https://fonts.googleapis.com/css2?family=Poppins:wght@500;600;800&family=Montserrat:wght@400;500&display=swap">
<style>
  :root {
    --brand-blue: #3a5fac;
    --accent-blue: #3fb0e8;
    --white: #ffffff;
    --photo-dark: #3a3a3a;
    --photo-mid: #555555;
  }
  * { box-sizing: border-box; margin: 0; padding: 0; }
  html, body { width: 1200px; height: 643px; overflow: hidden; background: var(--white); }
  .slide { position: relative; width: 1200px; height: 643px; overflow: hidden; background: var(--white); font-family: "Poppins", sans-serif; }
  .band-top { position: absolute; left: 0; top: 0; width: 918px; height: 124px; background: var(--brand-blue); }
  .band-left { position: absolute; left: 0; top: 0; width: 588px; height: 643px; background: var(--brand-blue); }
  .hero-photo {
    position: absolute; left: 588px; top: 124px; width: 496px; height: 519px;
    background: radial-gradient(ellipse at 55% 50%, var(--photo-mid) 0%, var(--photo-dark) 70%, #2c2c2c 100%);
  }
  .brand-name { position: absolute; left: 58px; top: 78px; color: var(--white); font-weight: 800; font-size: 28px; letter-spacing: 0.5px; }
  .nav { position: absolute; top: 46px; left: 0; }
  .nav-item { position: absolute; color: var(--white); font-weight: 600; font-size: 18px; letter-spacing: 1.4px; white-space: nowrap; transform: translateX(-50%); text-align: center; }
  .nav-item::after {
    content: ""; display: block; margin: 5px auto 0; width: 0; height: 0;
    border-left: 10px solid transparent; border-right: 10px solid transparent; border-top: 10px solid var(--accent-blue);
  }
  .nav-lessons { left: 567px; }
  .nav-menu { left: 693px; }
  .nav-glossary { left: 820px; }
  .duration { position: absolute; left: 1028px; top: 22px; width: 82px; height: 84px; }
  .title-panel { position: absolute; left: 0; top: 203px; width: 686px; height: 189px; background: var(--white); }
  .course-title { position: absolute; left: 54px; top: 30px; color: var(--brand-blue); font-weight: 800; font-size: 58px; line-height: 56px; letter-spacing: -0.3px; }
  .course-tags { position: absolute; top: 428px; left: 0; }
  .tag { position: absolute; display: flex; flex-direction: column; align-items: center; color: var(--white); font-family: "Montserrat", sans-serif; font-size: 10px; letter-spacing: 0.5px; transform: translateX(-50%); white-space: nowrap; }
  .tag svg { margin-bottom: 4px; }
  .tag-complexity { left: 91px; }
  .tag-audience { left: 196px; }
  .tag-interactive { left: 299px; top: -6px; }
  .start-button {
    position: absolute; left: 55px; top: 511px; width: 193px; height: 64px;
    border: 1.5px solid rgba(255,255,255,0.75); border-radius: 24px;
    display: flex; align-items: center; padding-left: 14px; gap: 10px;
    color: var(--white); font-weight: 800; font-size: 48px; letter-spacing: -0.5px; text-decoration: none;
  }
  .start-arrow { width: 0; height: 0; border-top: 11px solid transparent; border-bottom: 11px solid transparent; border-left: 12px solid var(--accent-blue); margin-top: 6px; }
</style>
</head>
<body>
<main class="slide">
  <div class="band-top"></div>
  <div class="band-left"></div>
  <div class="hero-photo" role="img" aria-label="Photo of a chalk fingerprint on a blackboard with a blue magnifying glass revealing binary digits"></div>

  <div class="brand-name">Norvale</div>

  <nav class="nav">
    <span class="nav-item nav-lessons">Lessons</span>
    <span class="nav-item nav-menu">Menu</span>
    <span class="nav-item nav-glossary">Glossary</span>
  </nav>

  <svg class="duration" viewBox="0 0 82 84" aria-label="30 minutes">
    <path d="M70 50 A34 34 0 1 1 48 9" fill="none" stroke="var(--brand-blue)" stroke-width="4"/>
    <polygon points="46,1 58,10 45,17" fill="var(--brand-blue)"/>
    <g stroke="var(--brand-blue)" stroke-width="1.5">
      <line x1="63" y1="18" x2="67" y2="15"/>
      <line x1="67" y1="24" x2="71" y2="22"/>
      <line x1="69" y1="30" x2="74" y2="29"/>
      <line x1="70" y1="36" x2="75" y2="36"/>
      <line x1="70" y1="42" x2="75" y2="43"/>
    </g>
    <text x="38" y="48" text-anchor="middle" font-family="Poppins, sans-serif" font-weight="800" font-size="25" fill="var(--brand-blue)">30</text>
    <text x="38" y="62" text-anchor="middle" font-family="Poppins, sans-serif" font-weight="600" font-size="13" fill="var(--brand-blue)">mins</text>
  </svg>

  <section class="title-panel">
    <h1 class="course-title">Handling sensitive<br>information</h1>
  </section>

  <div class="course-tags">
    <div class="tag tag-complexity">
      <svg width="32" height="34" viewBox="0 0 32 34" fill="none" stroke="#fff" stroke-width="2">
        <rect x="2" y="22" width="7" height="10" rx="2"/>
        <rect x="12" y="14" width="7" height="18" rx="2" fill="#fff"/>
        <rect x="22" y="2" width="7" height="30" rx="2"/>
      </svg>
      <span>Complexity</span>
    </div>
    <div class="tag tag-audience">
      <svg width="38" height="34" viewBox="0 0 38 34" fill="#fff">
        <circle cx="8" cy="12" r="4"/><circle cx="30" cy="12" r="4"/>
        <circle cx="19" cy="9" r="6"/>
        <path d="M1 30 q0-10 7-10 q5 0 6 4 v6z"/><path d="M37 30 q0-10-7-10 q-5 0-6 4 v6z"/>
        <path d="M10 32 q0-14 9-14 q9 0 9 14z"/>
      </svg>
      <span>All Audience</span>
    </div>
    <div class="tag tag-interactive">
      <svg width="58" height="44" viewBox="0 0 58 44" fill="#fff">
        <circle cx="20" cy="6" r="5"/><circle cx="40" cy="8" r="4"/><circle cx="8" cy="22" r="4"/>
        <circle cx="50" cy="22" r="6"/><circle cx="14" cy="34" r="5"/><circle cx="6" cy="12" r="2"/>
        <g stroke="#fff" stroke-width="1.2"><line x1="28" y1="22" x2="20" y2="6"/><line x1="28" y1="22" x2="40" y2="8"/><line x1="28" y1="22" x2="8" y2="22"/><line x1="28" y1="22" x2="50" y2="22"/><line x1="28" y1="22" x2="14" y2="34"/></g>
        <rect x="25" y="20" width="6" height="16" rx="3"/>
        <rect x="22" y="30" width="18" height="13" rx="3"/>
      </svg>
      <span>Interactive</span>
    </div>
  </div>

  <a class="start-button" href="#">start<span class="start-arrow"></span></a>
</main>
</body>
</html>
```